business card, stationary and envelopes for Insulation Company
Silver Otter Insulation
business card, stationary and envelopes for Insulation Company - Construction
Creative Brief
Bright & Fun-filled
Calvin Rudd
Sales Manager
7W.318 Maple Crest Drive Naperville, Illinois 60563
sales@silverotterinsulation-example.com
www.SilverOtterInsulation-example.com
Services Offered: Attic Insulation Wall Insulation Attic Ventilation Weatherization Attic Decontamination Insulation Removal Types of Insulation Cellulose Fiberglass Spray Foam Blown Batt

```html
<!DOCTYPE html>
<html lang="en">
<head>
<meta charset="utf-8">
<title>Silver Otter Insulation – Stationery</title>
<link href="https://fonts.googleapis.com/css2?family=Open+Sans:wght@400;600;700&display=swap" rel="stylesheet">
<style>
:root{
  --bg-dark:#2e2e2e;
  --bg-light:#6b6b6b;
  --green-dark:#3f7d1c;
  --green:#5d9e2a;
  --green-light:#a6d24e;
  --paper:#ffffff;
  --paper-shade:#f2f2f0;
  --accent-rose:#c9aaa2;
  --ink:#444;
  --ink-soft:#888;
  --label:#e6e6e6;
}
*{margin:0;padding:0;box-sizing:border-box}
html,body{width:1200px;height:437px;overflow:hidden}
body{
  font-family:"Open Sans",Arial,sans-serif;
  background:radial-gradient(ellipse at 55% 40%,var(--bg-light),var(--bg-dark) 80%);
  position:relative;
}
.item{position:absolute;box-shadow:0 3px 8px rgba(0,0,0,.45)}
.label{position:absolute;font-size:7px;color:var(--label);text-align:center;width:100%;left:0;bottom:-11px;white-space:nowrap}
.brand{font-weight:700;color:var(--green-dark);display:flex;align-items:center;gap:3px;white-space:nowrap}
.brand .mark{width:7px;height:7px;background:var(--green);display:inline-block;flex:none}
.brand.on-green{color:var(--paper)}
.brand.on-green .mark{background:var(--green-light)}

/* business cards */
.card{width:175px;height:62px;border-radius:4px}
.card-front{left:29px;top:150px;background:linear-gradient(135deg,var(--green-light),var(--green) 55%,var(--green-dark))}
.card-front .brand{position:absolute;left:8px;top:22px;font-size:6.5px;line-height:8px;white-space:normal;width:58px;align-items:flex-start}
.card-front .brand .mark{margin-top:1px}
.card-front .contact{position:absolute;left:80px;top:9px;font-size:3.5px;line-height:5.4px;color:var(--paper);white-space:nowrap}
.card-front .contact .name{font-weight:700;font-size:5px;line-height:6.5px}
.card-back{left:29px;top:262px;background:linear-gradient(135deg,var(--green),var(--green-dark))}
.card-back-white{left:29px;top:362px;background:var(--paper)}
.lists{position:absolute;inset:6px 8px;display:flex;gap:12px;font-size:4.3px;line-height:5.6px;white-space:nowrap}
.lists h4{font-size:5px;font-weight:700;margin-bottom:1px}
.card-back .lists{color:var(--paper)}
.card-back-white .lists{color:var(--ink)}
.card-back-white h4{color:var(--green-dark)}
.lists ul{list-style:none}
.lists li::before{content:"\2713 ";color:var(--green-light)}
.card-back-white li::before{color:var(--green)}

/* letterheads */
.letterhead{width:264px;height:386px;top:19px;background:var(--paper)}
.lh-1{left:228px}
.lh-2{left:516px}
.letterhead .brand{position:absolute;left:50%;transform:translateX(-50%);top:15px;font-size:7.5px}
.lh-address{position:absolute;left:186px;top:13px;font-size:3.2px;line-height:4.6px;color:var(--ink-soft);white-space:nowrap}
.lh-footer{position:absolute;left:0;bottom:0;width:100%;height:54px}

/* envelopes */
.envelope{width:360px;height:100px;left:828px;background:var(--paper);overflow:hidden}
.env-1{top:42px}
.env-2{top:152px;background:var(--paper-shade)}
.env-3{top:256px;height:80px}
.env-4{top:342px;height:84px;width:180px}
.envelope svg{position:absolute;left:0;top:0;width:100%;height:100%}
.env-brand{position:absolute;left:50%;transform:translateX(-50%);top:22px;font-size:7px}
.env-3 .brand{position:absolute;left:78px;top:36px;font-size:6px}
.env-4 .brand{position:absolute;left:8px;top:8px;font-size:5px}
.env-label{position:absolute;right:12px;top:24px;font-size:7px;color:var(--label)}
</style>
</head>
<body>

<div class="item card card-front">
  <div class="brand on-green"><span class="mark"></span><span>Silver Otter Insulation</span></div>
  <div class="contact">
    <div class="name">Calvin Rudd</div>
    <div>Sales Manager</div>
    <div>7W.318 Maple Crest Drive</div>
    <div>Naperville, Illinois 60563</div>
    <div>sales@silverotterinsulation-example.com</div>
    <div>www.SilverOtterInsulation-example.com</div>
  </div>
  <div class="label">Business Card</div>
</div>

<div class="item card card-back">
  <div class="lists">
    <div><h4>Services Offered</h4><ul><li>Attic Insulation</li><li>Wall Insulation</li><li>Attic Ventilation</li><li>Weatherization</li><li>Attic Decontamination</li><li>Insulation Removal</li></ul></div>
    <div><h4>Types of Insulation</h4><ul><li>Cellulose</li><li>Fiberglass</li><li>Spray Foam</li><li>Blown</li><li>Batt</li></ul></div>
  </div>
  <div class="label">Business Card Back</div>
</div>

<div class="item card card-back-white">
  <div class="lists">
    <div><h4>Services Offered</h4><ul><li>Attic Insulation</li><li>Wall Insulation</li><li>Attic Ventilation</li><li>Weatherization</li><li>Attic Decontamination</li><li>Insulation Removal</li></ul></div>
    <div><h4>Types of Insulation</h4><ul><li>Cellulose</li><li>Fiberglass</li><li>Spray Foam</li><li>Blown</li><li>Batt</li></ul></div>
  </div>
  <div class="label">Business Card Back 2</div>
</div>

<div class="item letterhead lh-1">
  <div class="brand"><span class="mark"></span>Silver Otter Insulation</div>
  <div class="lh-address">7W.318 Maple Crest Drive<br>Naperville, Illinois 60563<br>sales@silverotterinsulation-example.com<br>www.SilverOtterInsulation-example.com</div>
  <svg class="lh-footer" viewBox="0 0 264 54" preserveAspectRatio="none">
    <defs><linearGradient id="lhg1" x1="0" x2="1"><stop offset="0" stop-color="#a6d24e"/><stop offset=".5" stop-color="#5d9e2a"/><stop offset="1" stop-color="#3f7d1c"/></linearGradient></defs>
    <path d="M0 22 Q132 2 264 26 L264 30 Q132 8 0 28Z" fill="#c9aaa2"/>
    <path d="M0 32 Q132 12 264 34 L264 54 L0 54Z" fill="url(#lhg1)"/>
  </svg>
  <div class="label">Letterhead Page 1</div>
</div>

<div class="item letterhead lh-2">
  <div class="brand"><span class="mark"></span>Silver Otter Insulation</div>
  <svg class="lh-footer" viewBox="0 0 264 54" preserveAspectRatio="none">
    <defs><linearGradient id="lhg2" x1="0" x2="1"><stop offset="0" stop-color="#a6d24e"/><stop offset=".5" stop-color="#5d9e2a"/><stop offset="1" stop-color="#3f7d1c"/></linearGradient></defs>
    <path d="M0 22 Q132 2 264 26 L264 30 Q132 8 0 28Z" fill="#c9aaa2"/>
    <path d="M0 32 Q132 12 264 34 L264 54 L0 54Z" fill="url(#lhg2)"/>
  </svg>
  <div class="label">Letterhead Page 2</div>
</div>

<div class="env-label">Envelope Front &amp; Back</div>

<div class="item envelope env-1">
  <svg viewBox="0 0 360 100" preserveAspectRatio="none">
    <defs><linearGradient id="eg1" x1="0" x2="1"><stop offset="0" stop-color="#3f7d1c"/><stop offset=".5" stop-color="#a6d24e"/><stop offset="1" stop-color="#3f7d1c"/></linearGradient></defs>
    <path d="M0 0 H360 V22 Q180 58 0 22Z" fill="url(#eg1)"/>
    <path d="M0 100 L180 52 L360 100" fill="none" stroke="#ddd" stroke-width="1"/>
  </svg>
  <div class="brand env-brand"><span class="mark"></span>Silver Otter Insulation</div>
</div>

<div class="item envelope env-2">
  <svg viewBox="0 0 360 100" preserveAspectRatio="none">
    <path d="M0 0 L180 58 L360 0Z" fill="#fff" stroke="#ddd"/>
    <path d="M0 0 H360 V10 Q180 30 0 10Z" fill="#5d9e2a"/>
  </svg>
  <div class="brand env-brand" style="top:30px"><span class="mark"></span>Silver Otter Insulation</div>
</div>

<div class="item envelope env-3">
  <svg viewBox="0 0 360 80" preserveAspectRatio="none">
    <path d="M0 0 L180 38 L360 0" fill="none" stroke="#e2e2e2"/>
    <path d="M0 70 Q180 56 360 70 V80 H0Z" fill="#5d9e2a"/>
  </svg>
  <div class="brand"><span class="mark"></span>Silver Otter Insulation</div>
</div>

<div class="item envelope env-4">
  <svg viewBox="0 0 180 84" preserveAspectRatio="none">
    <path d="M0 72 Q90 58 180 72 V84 H0Z" fill="#5d9e2a"/>
  </svg>
  <div class="brand"><span class="mark"></span>Silver Otter Insulation</div>
</div>

</body>
</html>
```